Martial Art workout site needs web page design

We need a web page designed for our new martial art web site that presents innovated, monthly workouts, done by beautiful models
Web page should include
- a home page
- Page for the monthly workout
- Gallery page for the models (pics & video)
-Archived page for past workout
- Page to sign up for monthly updates
- Sponsor Page

Martial Art

```html
<!DOCTYPE html>
<html lang="en">
<head>
<meta charset="utf-8">
<title>Martial Art workout</title>
<link href="https://fonts.googleapis.com/css2?family=PT+Sans:ital,wght@0,400;0,700;1,400;1,700&display=swap" rel="stylesheet">
<style>
:root{
  --page-bg:#e8eaed;
  --panel:#f3f4f6;
  --title:#333f48;
  --text:#1e1e1e;
  --muted:#3c4650;
  --nav-top:#eea6c8;
  --nav-bottom:#de82ae;
  --nav-active:#2f86c6;
  --diet:#2f86b3;
  --diet-ink:#1d5783;
  --eco:#b0476a;
  --eco-ink:#3c5f9a;
  --separate:#5b9a2a;
  --separate-ink:#2d5f8a;
  --healthy:#eb9a12;
  --healthy-ink:#274f86;
  --heading:#1f5f95;
  --bullet:#d1427b;
  --btn-top:#d6dbe0;
  --btn-bottom:#a7b0b9;
}
*{box-sizing:border-box;margin:0;padding:0}
html,body{width:1189px;height:1200px;overflow:hidden}
body{position:relative;background:linear-gradient(180deg,#eef0f2,var(--page-bg));font-family:"PT Sans",sans-serif;color:var(--text)}
.site-title{position:absolute;left:62px;top:88px;font-size:50px;font-weight:700;font-style:italic;color:var(--title);letter-spacing:1px}
.tagline{position:absolute;left:64px;top:154px;font-size:15px;color:#222}
.header-photo{position:absolute;left:811px;top:61px;width:265px;height:231px;background:linear-gradient(135deg,#ffffff,#dfe2e6);border:4px solid #cfd3d8;box-shadow:0 2px 6px rgba(0,0,0,.25)}
.header-photo-figure{position:absolute;left:800px;top:44px;width:315px;height:260px;background:radial-gradient(ellipse at 55% 45%,rgba(212,150,120,.55),rgba(196,40,40,.25) 55%,transparent 75%)}
.main-nav{position:absolute;left:48px;top:251px;width:1085px;height:59px;border-radius:5px;background:linear-gradient(180deg,var(--nav-top),var(--nav-bottom));box-shadow:0 1px 3px rgba(0,0,0,.2)}
.main-nav a{position:absolute;top:9px;height:40px;line-height:40px;font-size:14px;color:#1b1b1b;text-decoration:none;letter-spacing:.5px;text-align:center;width:130px}
.main-nav a.active{left:197px;width:111px;background:linear-gradient(180deg,#3f9ad8,var(--nav-active));color:#fff;border:1px solid #1f6fa8;border-radius:2px}
.content-panel{position:absolute;left:48px;top:319px;width:1085px;height:890px;background:rgba(247,248,250,.8);border:1px solid #dcdfe3}
.feature-photo{position:absolute;top:341px;width:254px;height:254px;border:1px solid #b9c2cc;background:#fff}
.feature-photo span{position:absolute;inset:6px;display:block}
.feature-band{position:absolute;top:609px;width:256px;height:47px;line-height:47px;text-align:center;font-size:17px;letter-spacing:.3px}
.feature-text{position:absolute;top:682px;width:230px;font-size:14.5px;line-height:17.6px;text-align:justify}
.btn{position:absolute;width:149px;height:31px;line-height:30px;text-align:center;font-size:14px;letter-spacing:.5px;color:#111;background:linear-gradient(180deg,var(--btn-top),var(--btn-bottom));border:1px solid #8e979f}
.tips-list{position:absolute;left:885px;top:684px;font-size:14px;font-style:italic;color:var(--muted);padding-left:24px}
.tips-list li{height:32.5px;padding-left:8px}
.article-heading{position:absolute;left:72px;top:862px;font-size:27px;font-weight:700;color:var(--heading);letter-spacing:.4px}
.article-photo{position:absolute;left:72px;top:909px;width:242px;height:228px;border:1px solid #b9c2cc;background:linear-gradient(180deg,#bfe0f4 0%,#e9f2f6 55%,#d9c9a7 100%)}
.article-text{position:absolute;left:338px;top:908px;width:506px;font-size:14.5px;line-height:17.6px;text-align:justify}
.article-text p+p{margin-top:9px}
.side-links{position:absolute;left:870px;top:851px;list-style:none;font-size:14px;font-style:italic;color:var(--muted)}
.side-links li{height:32px;padding-left:18px;position:relative}
.side-links li::before{content:"";position:absolute;left:0;top:6px;width:6px;height:7px;border-left:2px dotted var(--bullet);border-right:2px dotted var(--bullet)}
.copyright{position:absolute;left:0;width:1160px;top:1161px;text-align:center;font-size:14px;letter-spacing:.5px}
</style>
</head>
<body>
<header>
  <h1 class="site-title">Martial Art workout</h1>
  <p class="tagline">your personal assistants on the way to health</p>
  <div class="header-photo" role="img" aria-label="Framed photo of a fighter in red shorts throwing a high kick"></div>
  <div class="header-photo-figure" role="img" aria-label="Fighter stepping out of the frame"></div>
</header>

<nav class="main-nav">
  <a class="active" href="#">HOME</a>
  <a href="#" style="left:365px">GALLERY</a>
  <a href="#" style="left:511px">ARCHIVED</a>
  <a href="#" style="left:658px">SIGN UP</a>
  <a href="#" style="left:801px">SPONSOR</a>
</nav>

<main class="content-panel"></main>

<section class="features">
  <div class="feature-photo" style="left:60px"><span role="img" aria-label="Athlete in black performing a high kick" style="background:linear-gradient(180deg,#ffffff,#eceae8)"></span></div>
  <div class="feature-photo" style="left:329px"><span role="img" aria-label="Two fighters sparring with a kick" style="background:linear-gradient(180deg,#ffffff,#e8e4e2)"></span></div>
  <div class="feature-photo" style="left:597px"><span role="img" aria-label="Boxers trading punches with gloves" style="background:linear-gradient(180deg,#d9d4d0,#3a3434 70%,#b63a2a)"></span></div>
  <div class="feature-photo" style="left:864px"><span role="img" aria-label="Fit man and woman posing in training gear" style="background:linear-gradient(180deg,#f4f4f4,#c9a48c 45%,#2c2c30)"></span></div>

  <div class="feature-band" style="left:60px;background:var(--diet);color:var(--diet-ink)">DIET PLANNING</div>
  <div class="feature-band" style="left:329px;background:var(--eco);color:var(--eco-ink)">ECO-FRIENDLY EATING</div>
  <div class="feature-band" style="left:597px;background:var(--separate);color:var(--separate-ink)">SEPARATE EATING</div>
  <div class="feature-band" style="left:864px;background:var(--healthy);color:var(--healthy-ink)">HEALTHY NUTRITION</div>

  <p class="feature-text" style="left:72px">Lorem ipsum dolor sit amet, consectetur adipiscing elit. Etiam pharetra, tellus sit amet congue vulputate, nisi erat iaculis nibh, vitae feugiat sapien ante eget.</p>
  <p class="feature-text" style="left:340px">Cras elit nisl, rhoncus nec iaculis ultricies, feugiat eget sapien. Pellentesque ac felis tellus. Aenean sollicitudin imperdiet arcu, vitae dignissim.</p>
  <p class="feature-text" style="left:609px">Phasellus elit dolor, porttitor id consectetur sit amet, posuere id magna. Lorem ipsum dolor sit amet, consectetur adipiscing elit. Suspendisse pharetra auctor.</p>

  <a class="btn" style="left:72px;top:794px">READ MORE</a>
  <a class="btn" style="left:340px;top:794px">READ MORE</a>
  <a class="btn" style="left:609px;top:794px">READ MORE</a>

  <ol class="tips-list">
    <li>Sed at turpis vel ipsum.</li>
    <li>Praesent neque turpis.</li>
    <li>Nunc aliquet ultrices tortor.</li>
    <li>Mauris aliquet metus a leo.</li>
  </ol>
</section>

<article>
  <h2 class="article-heading">Essentials of Healthy Eating to Live Longer and Happily</h2>
  <div class="article-photo" role="img" aria-label="Smiling fit couple standing back to back on a beach"></div>
  <div class="article-text">
    <p>Fusce ornare elit nisl, feugiat bibendum lorem. Vivamus pretium dictum sem vel laoreet. In fringilla pharetra purus, semper vulputate ligula cursus in. Donec at nunc nec dui laoreet porta eu eu ipsum. Sed eget lacus sit amet risus elementum dictum.</p>
    <p>Pellentesque sit amet imperdiet nunc. Aenean tellus mi, adipiscing sit amet laoreet eget, lobortis quis nisl. Quisque volutpat urna orci, id gravida nisi. Nullam posuere interdum est sit amet aliquam. Suspendisse malesuada metus ac enim feugiat commodo.</p>
  </div>
  <a class="btn" style="left:338px;top:1080px">READ MORE</a>
</article>

<aside>
  <ul class="side-links">
    <li>Proin nulla nibh, tempor.</li>
    <li>Vestibulum at nunc risus.</li>
    <li>Aliquam erat volutpat.</li>
    <li>Nullam quis lorem metus.</li>
    <li>Phasellus ut nibh tortor.</li>
    <li>Integer commodo nisi eget.</li>
    <li>In vitae tincidunt felis.</li>
    <li>Donec in dolor a libero.</li>
    <li>Ut vel libero a arcu mattis.</li>
  </ul>
</aside>

<footer class="copyright">Copyright @.</footer>
</body>
</html>
```